Plakat-Design für kleine deutsche Immobilien- und Reiseveranstalter-Firma
Zielgruppe
Kleine deutsche Immobilien- und Reiseveranstalter-Firma, spezialisiert auf Italien. In Italien sind es Immobilienbesitzer, die aus versch. Gründen hoffen an Ausländer zu verkaufen/vermieten ( Alter ca. ab 35-40)
Aufgabenstellung
Um neue Immo-Besitzer anzusprechen, lassen wir in verschiedenen Gemeinden in der Nordtoskana Plakate gegen Gebühr kleben ( 70 x 100, meistens 1 bis 2 Wochen)
Text auf Italienisch
Was an Text rein muss( falls Sie es anders mitteilen wollen, bin ich gerne bereit es zu diskutieren)
VUOI VENDERE CASA A STRANIERI O AFFITTARLA A TURISTI ? (Übersetzung ca.:= wollen Sie Ihre Immobilie an Ausländer verkaufen oder an Touristen vermieten?)
Serafon
Germania – info@serafon-beispiel.de + 49 7214 3817204
Italia – 0472 – 316094, Cell.: 377 – 4102968, 331- 74 20539,
www.serafonhaus-beispiel.com
www.serafonmiete-beispiel.com
Der Poster, den man meistens im Vorbeifahren sieht, soll springt sofort ins Auge , fast aufdringlich. Man kann mit Farben oder Bildern (oder beiden) arbeiten. Stechende Farben, sonst minimalistisch einfach. (??)
Erfahrung zeigt, daß die beiden Mobile Nummern (Cell.:) mehr sichtbar sein könnten. Ich kann zwei letzte zeigen, aber ungern, weil sie mir nicht gefallen und Neues – besseres suche.
PS: habe mal so was wie Guerilla -Marketing versucht – wurde nicht verstanden.
Bilder kann ich nach Wunsch liefern.

```html
<!DOCTYPE html>
<html lang="it">
<head>
<meta charset="utf-8">
<title>Serafon – Plakat</title>
<link href="https://fonts.googleapis.com/css2?family=Pathway+Gothic+One&display=swap" rel="stylesheet">
<style>
  :root {
    --page-bg: #d9d9d5;
    --paper: #ebebe8;
    --lime: #a6bb1c;
    --lime-dark: #8ea214;
    --magenta: #c31d62;
    --ink: #1d1d1b;
    --white: #ffffff;
    --illustration-light: #dcdcd6;
  }
  * { box-sizing: border-box; margin: 0; padding: 0; }
  html, body {
    width: 1200px;
    height: 900px;
    overflow: hidden;
    background: var(--page-bg);
    font-family: "Pathway Gothic One", "Arial Narrow", sans-serif;
  }
  .poster {
    position: absolute;
    left: 294px;
    top: 20px;
    width: 612px;
    height: 860px;
    background: var(--paper);
    overflow: hidden;
    box-shadow: 0 2px 10px rgba(0,0,0,0.12);
  }
  .accent-circle {
    position: absolute;
    left: 190px;
    top: 88px;
    width: 688px;
    height: 688px;
    border-radius: 50%;
    background: var(--magenta);
  }
  .illustration {
    position: absolute;
    border-radius: 10px;
    background: linear-gradient(160deg, var(--illustration-light) 0%, var(--lime) 100%);
    opacity: 0.9;
  }
  .illustration--apartment { left: 44px; top: 62px; width: 204px; height: 253px; }
  .illustration--cottage   { left: 368px; top: 16px; width: 182px; height: 144px; }
  .illustration--villa     { left: 368px; top: 297px; width: 204px; height: 146px; }
  .illustration--care      { left: 359px; top: 603px; width: 164px; height: 195px; }

  .question {
    position: absolute;
    width: 293px;
    padding: 10px 14px;
    background: var(--lime);
    border: 3px solid var(--ink);
    border-radius: 14px;
    box-shadow: 5px 5px 0 var(--white), 6px 7px 0 var(--ink);
    color: var(--white);
    -webkit-text-stroke: 1px var(--ink);
    text-align: center;
    line-height: 1.0;
    letter-spacing: 1px;
  }
  .question--house   { left: 297px; top: 158px; font-size: 44px; padding: 18px 14px; transform: rotate(4deg); }
  .question--sell    { left: 33px;  top: 296px; font-size: 36px; transform: rotate(-9deg); }
  .question--rent    { left: 270px; top: 468px; font-size: 36px; transform: rotate(2deg); }

  .brand {
    position: absolute;
    left: 24px;
    top: 560px;
  }
  .brand__tagline {
    margin-left: 38px;
    font-size: 30px;
    color: var(--lime-dark);
    line-height: 1;
  }
  .brand__row {
    display: flex;
    align-items: center;
    gap: 10px;
  }
  .brand__dot {
    width: 28px;
    height: 28px;
    border-radius: 50%;
    background: var(--lime-dark);
  }
  .brand__name {
    font-size: 54px;
    color: var(--ink);
    line-height: 1;
    letter-spacing: 1px;
  }
  .contacts {
    position: absolute;
    left: 64px;
    top: 652px;
    list-style: none;
    font-size: 29px;
    line-height: 38px;
    color: var(--ink);
    letter-spacing: 0.5px;
  }
  .websites {
    position: absolute;
    left: 0;
    right: 0;
    top: 826px;
    text-align: center;
    font-size: 23px;
    color: var(--ink);
    letter-spacing: 0.6px;
  }
</style>
</head>
<body>
  <main class="poster">
    <div class="accent-circle"></div>

    <div class="illustration illustration--apartment" role="img" aria-label="Linienillustration eines mehrstöckigen Wohnhauses in Grün"></div>
    <div class="illustration illustration--cottage" role="img" aria-label="Linienillustration eines kleinen Hauses mit Schornstein"></div>
    <div class="illustration illustration--villa" role="img" aria-label="Linienillustration eines Einfamilienhauses mit Garage"></div>
    <div class="illustration illustration--care" role="img" aria-label="Illustration einer Hand, die ein Haus trägt"></div>

    <p class="question question--house">Hai una casa?</p>
    <p class="question question--sell">Vuoi vendere<br>a stranieri?</p>
    <p class="question question--rent">Vuoi affittarla<br>a turisti?</p>

    <div class="brand">
      <p class="brand__tagline">Ti aiutiamo</p>
      <div class="brand__row">
        <span class="brand__dot"></span>
        <span class="brand__name">Serafon</span>
      </div>
    </div>

    <ul class="contacts">
      <li>info@serafon-beispiel.de</li>
      <li>+ 49 7214 3817204</li>
      <li>0472 – 316094</li>
      <li>377 – 4102968</li>
    </ul>

    <p class="websites">www.serafonhaus-beispiel.com, www.serafonmiete-beispiel.com</p>
  </main>
</body>
</html>
```